Business price tag design for Furniture Business

Hello,

I have developed a tag for a home furniture business and need 1 more creative template. Please see attachment. I need the template to be very appealing.

Requirements:

1.Tag dimensions needs to be about the same as attached tag.
2. Tag design needs to be suitable for a home furniture business.
3. Tag needs to have locations for the following: Item Title, Now Price, Was Price, Product Number.
4. "The black shape at the bottom of attached tag could be removed.

I have no requirements on colors, but something professional is needed, preferably white background to reduce print ink consumption.

Please see attachment for clarification.

Industry/Entity Type

Retail

Font styles to use
Serif
Sans Serif

Requirements
Must have
• Please see Project Description.
Nice to have

```html
<!DOCTYPE html>
<html lang="en">
<head>
<meta charset="utf-8">
<title>Allied Home Furnishings – Price Tag</title>
<link href="https://fonts.googleapis.com/css2?family=Poppins:ital,wght@0,500;0,600;0,700;1,600;1,700&display=swap" rel="stylesheet">
<style>
  :root {
    --paper: #ffffff;
    --ink: #111111;
    --accent: #e35a5a;
    --frame: #2a2a2a;
    --photo-light: #f1f1f1;
    --photo-mid: #c9c9c9;
    --photo-dark: #9a9a9a;
  }
  * { margin: 0; padding: 0; box-sizing: border-box; }
  html, body { width: 1200px; height: 2380px; overflow: hidden; background: var(--paper); }
  .tag {
    position: relative;
    width: 1200px;
    height: 2380px;
    background: var(--paper);
    font-family: "Poppins", sans-serif;
    color: var(--ink);
    overflow: hidden;
  }
  .tag__frame {
    position: absolute;
    left: 16px; top: 16px;
    width: 1168px; height: 2324px;
    border: 4px solid var(--frame);
  }
  .tag__photo {
    position: absolute;
    left: 0; top: 0;
    width: 1200px; height: 900px;
    background: linear-gradient(160deg, var(--photo-mid) 0%, var(--photo-light) 38%, var(--paper) 75%);
  }
  .tag__sweep {
    position: absolute;
    left: 0; top: 0;
    width: 1200px; height: 900px;
  }
  .tag__brand {
    position: absolute;
    left: 32px; top: 88px;
    width: 1136px; height: 88px;
    background: var(--accent);
    color: var(--paper);
    font-weight: 600;
    font-size: 60px;
    letter-spacing: 4px;
    line-height: 88px;
    text-align: center;
    white-space: nowrap;
  }
  .item-title {
    position: absolute;
    left: 48px; top: 540px;
    font-weight: 600;
    font-size: 34px;
    letter-spacing: 2px;
  }
  .item-number {
    position: absolute;
    left: 50px; top: 672px;
    font-weight: 600;
    font-style: italic;
    font-size: 32px;
    letter-spacing: 2px;
  }
  .price-block {
    position: absolute;
    left: 0; width: 1200px;
    text-align: center;
  }
  .was-label { top: 1010px; font-weight: 600; font-size: 66px; letter-spacing: 8px; }
  .was-price { top: 1080px; font-weight: 700; font-size: 160px; letter-spacing: 24px; line-height: 1.1; }
  .now-label { top: 1332px; font-weight: 600; font-size: 66px; letter-spacing: 7px; }
  .now-label em { font-style: italic; }
  .now-price {
    position: absolute;
    left: 240px; top: 1432px;
    width: 744px; height: 160px;
    background: var(--accent);
    color: var(--paper);
    font-weight: 700;
    font-style: italic;
    font-size: 150px;
    letter-spacing: 20px;
    line-height: 160px;
    text-align: center;
  }
  .saving { top: 1688px; font-weight: 600; font-size: 52px; letter-spacing: 10px; }
  .saving em { color: var(--accent); font-style: italic; font-weight: 700; }
</style>
</head>
<body>
  <main class="tag">
    <div class="tag__photo" role="img" aria-label="Soft grey photograph of a furnished bedroom interior"></div>
    <svg class="tag__sweep" viewBox="0 0 1200 900" aria-hidden="true">
      <path d="M0 780 C 260 560, 700 320, 1200 330 L 1200 900 L 0 900 Z" fill="#ffffff" fill-opacity="0.96"/>
      <circle cx="1060" cy="660" r="140" fill="none" stroke="#e6e6e6" stroke-width="6"/>
      <circle cx="1180" cy="520" r="120" fill="none" stroke="#ececec" stroke-width="6"/>
    </svg>
    <div class="tag__frame"></div>

    <div class="tag__brand">ALLIED HOME FURNISHINGS</div>

    <p class="item-title">BLACK QUEEN BED</p>
    <p class="item-number">B4350</p>

    <p class="price-block was-label">COMPARE PRICE AT</p>
    <p class="price-block was-price">$500</p>
    <p class="price-block now-label">NOW PRICED <em>AT ONLY</em></p>
    <p class="now-price">$450!</p>
    <p class="price-block saving">YOU SAVE <em>$50!</em></p>
  </main>
</body>
</html>
```